Labels for Bees Wax Candles & Honey Jars

We need labels for jars of natural honey. Most of our jars are square and the labels about 2" by 2".

Also we make bees wax candles of various sizes. We wish to wrap th enables around the circular candles which are between 2" and 3" in diameter... thus another have inch per label so they can be attached adhesively. The candles also vary in height... therefor th enables need to be 1.5", 2" and 3" in height.

We ar elooking for a very artistic and simple label that may include vibrant colors.
The name of our company must be displayed.. Candles by Morton and for the Honey.... Morton's All Natural Honey

The labels will be used for both Honey Jars as well as Bees Wax candles. There will be various sizes but that is something that can be adjusted after the initial design is approved. The Honey Jars should read "Natural Honey by Morton" and the Candle labels should read "Natural Bees Wax Candles by Morton" I am interested in simple, colorful, legible, and arty labels that pertain to bees and the natural environment. Hope this helps. We may also use a similar design on our web page. The size of the label on the honey will be 2" by 2" and the candles will vary.

Target Market(s)

Individual that purchase natural and organic products.

Requirements
Must have
• Labels should be very creative but legible and the emphasis on the candles should be all natural bees wax and the emphasis on the honey should be all natural honey. We are talking about the same design but different sizes and names.
Nice to have
• brillant colors and artistic

```html
<!DOCTYPE html>
<html lang="en">
<head>
<meta charset="utf-8">
<title>Natural Honey by Morton — Jar Label</title>
<link href="https://fonts.googleapis.com/css2?family=Gelasio:wght@400;500&display=swap" rel="stylesheet">
<style>
  :root {
    --page: #ffffff;
    --lime: #cadc2a;
    --lime-light: #d4e236;
    --honey-orange: #f58b22;
    --bee-dark: #6b4a1c;
    --bee-gold: #e6c92c;
    --sun-yellow: #ece619;
    --title-purple: #4c4c9e;
    --maker-red: #e6212a;
    --tagline: #ede52c;
  }
  html, body {
    margin: 0;
    padding: 0;
    width: 1200px;
    height: 1000px;
    overflow: hidden;
    background: var(--page);
  }
  .canvas {
    position: relative;
    width: 1200px;
    height: 1000px;
  }
  .label {
    position: absolute;
    left: 298px;
    top: 111px;
    width: 634px;
    height: 632px;
    overflow: hidden;
    background: var(--lime);
  }
  .label-art {
    position: absolute;
    inset: 0;
  }
  .title {
    position: absolute;
    left: 0;
    margin: 0;
    text-align: right;
    font-family: "Gelasio", Georgia, serif;
    line-height: 1;
    white-space: nowrap;
  }
  .title-product {
    top: 112px;
    width: 580px;
    font-size: 68px;
    font-weight: 500;
    color: var(--title-purple);
  }
  .title-maker {
    top: 180px;
    width: 575px;
    font-size: 54px;
    font-weight: 400;
    color: var(--maker-red);
  }
  .taglines {
    position: absolute;
    left: 0;
    top: 0;
    width: 532px;
    height: 632px;
    margin: 0;
    padding: 0;
    list-style: none;
    font-family: "Gelasio", Georgia, serif;
    color: var(--tagline);
    opacity: 0.85;
  }
  .taglines li {
    position: absolute;
    right: 0;
    line-height: 1;
    white-space: nowrap;
  }
  .taglines .t1 { top: 318px; font-size: 20px; }
  .taglines .t2 { top: 350px; font-size: 24px; }
  .taglines .t3 { top: 390px; font-size: 29px; letter-spacing: 0.5px; }
  .taglines .t4 { top: 438px; font-size: 35px; letter-spacing: 1px; }
  .taglines .t5 { top: 494px; font-size: 42px; letter-spacing: 1.2px; }
</style>
</head>
<body>
<div class="canvas">
  <section class="label" aria-label="Natural Honey by Morton jar label">
    <svg class="label-art" width="634" height="632" viewBox="0 0 634 632">
      <defs>
        <linearGradient id="bee-tone" x1="0" y1="0" x2="1" y2="1">
          <stop offset="0" stop-color="var(--bee-gold)"/>
          <stop offset="1" stop-color="var(--bee-dark)"/>
        </linearGradient>
      </defs>
      <!-- sunlit frame along the right and bottom edges -->
      <rect class="edge-band" x="570" y="230" width="38" height="372" fill="var(--sun-yellow)" opacity="0.8"/>
      <rect class="edge-band" x="40" y="562" width="568" height="40" fill="var(--sun-yellow)" opacity="0.8"/>
      <rect class="edge-glow" x="30" y="610" width="604" height="22" fill="var(--lime-light)" opacity="0.6"/>

      <!-- honeycomb field -->
      <polygon role="img" aria-label="Orange honeycomb pattern"
        points="0,0 495,0 548,35 555,95 510,125 505,225 408,232 300,240 250,250 270,300 240,330 120,360 0,380"
        fill="var(--honey-orange)"/>

      <!-- honeybee area -->
      <path role="img" aria-label="Illustration of a honeybee crawling on the comb"
        d="M0,200 C60,178 140,172 190,190 C228,210 240,300 236,372 C200,400 120,432 50,452 C25,460 10,468 0,476 Z"
        fill="url(#bee-tone)" opacity="0.9"/>

      <!-- hanging holes -->
      <g class="hole">
        <circle cx="585" cy="299" r="23" fill="var(--sun-yellow)"/>
        <circle cx="585" cy="299" r="17" fill="var(--page)"/>
      </g>
      <g class="hole">
        <circle cx="113" cy="580" r="23" fill="var(--sun-yellow)"/>
        <circle cx="113" cy="580" r="17" fill="var(--page)"/>
      </g>
    </svg>

    <h1 class="title title-product">Natural Honey</h1>
    <p class="title title-maker">by Morton</p>

    <ul class="taglines">
      <li class="t1">all natural honey</li>
      <li class="t2">all natural honey</li>
      <li class="t3">all natural honey</li>
      <li class="t4">all natural honey</li>
      <li class="t5">all natural honey</li>
    </ul>
  </section>
</div>
</body>
</html>
```